Real Estate Business Cards

Looking for a clean, sharp and professional look for our Real Estate investment Fund that invests in Multi Family Apartment buildings.

Target Market(s)

Real Estate Fund

Industry/Entity Type

Real Estate

Contact Information for Business Card

Company Description: Real Estate Investment Fund
Company Name: RKW Holdings
Name: Marcus Olvane
Cell: (917) 482-0657
Email: marcus@rkwholdings-example.com
Website: www.rkwholdings-example.com
Address: 418, 9th Street, Brooklyn NY 11218

Colors

Designer to choose colors to be used in the design.

Requirements
Nice to have
• Colors to match logo

```html
<!DOCTYPE html>
<html lang="en">
<head>
<meta charset="utf-8">
<title>RKW Holdings – Business Cards</title>
<link rel="stylesheet" href="https://fonts.googleapis.com/css2?family=EB+Garamond:wght@400&family=Roboto:wght@400;700&display=swap">
<style>
  :root {
    --brand-blue: #0a6aa6;
    --name-blue: #2f6fa8;
    --ink: #2b2b2b;
    --paper: #ffffff;
    --backdrop: #e9ecef;
  }
  * { box-sizing: border-box; margin: 0; padding: 0; }
  html, body { width: 1200px; height: 1020px; overflow: hidden; }
  body {
    background: var(--backdrop);
    position: relative;
    font-family: "Roboto", Arial, sans-serif;
  }
  .card {
    position: absolute;
    left: 210px;
    width: 780px;
    height: 448px;
    overflow: hidden;
  }
  .card--front { top: 32px; background: var(--brand-blue); }
  .card--back { top: 540px; background: var(--paper); }

  .front-pattern {
    position: absolute; inset: 0;
    background: var(--brand-blue);
  }
  .front-brand {
    position: absolute;
    left: 0; right: 0; top: 270px;
    display: flex; align-items: center; justify-content: center; gap: 18px;
  }
  .brand-mark {
    width: 20px; height: 20px;
    background: var(--paper);
  }
  .front-brand .brand-name {
    font-family: "EB Garamond", Georgia, serif;
    font-weight: 400;
    font-size: 52px;
    letter-spacing: 1px;
    color: var(--paper);
  }

  .back-brand {
    position: absolute;
    left: 25px; top: 158px;
    font-family: "EB Garamond", Georgia, serif;
    font-weight: 400;
    font-size: 34px;
    letter-spacing: 0.5px;
    color: var(--brand-blue);
  }
  .holder {
    position: absolute;
    right: 27px; top: 230px;
    text-align: right;
  }
  .holder-name {
    font-weight: 700;
    font-size: 31px;
    color: var(--name-blue);
    letter-spacing: 0.3px;
    line-height: 1.1;
  }
  .holder-role {
    font-size: 20px;
    color: var(--ink);
    margin-top: 3px;
  }
  .divider {
    position: absolute;
    left: 25px; right: 27px; top: 307px;
    height: 2px;
    background: var(--name-blue);
  }
  .contacts {
    position: absolute;
    left: 25px; top: 322px;
    list-style: none;
  }
  .contacts li {
    display: flex; align-items: center; gap: 10px;
    font-size: 21px;
    color: var(--ink);
    height: 31px;
  }
  .contacts svg { width: 16px; height: 16px; flex: none; }
  .address {
    position: absolute;
    right: 27px; top: 355px;
    text-align: right;
    font-size: 21px;
    line-height: 30px;
    color: var(--ink);
    font-style: normal;
  }
  .base-band {
    position: absolute;
    left: 0; right: 0; bottom: 0;
    height: 14px;
    background: var(--brand-blue);
  }
  .base-band-notch {
    position: absolute;
    left: 386px; bottom: 0;
    width: 14px; height: 14px;
    background: var(--paper);
  }
</style>
</head>
<body>
  <section class="card card--front" aria-label="Card front">
    <div class="front-pattern" role="img" aria-label="Faint repeating diamond pattern on brand blue"></div>
    <div class="front-brand">
      <span class="brand-mark"></span>
      <span class="brand-name">RKW HOLDINGS</span>
    </div>
  </section>

  <section class="card card--back" aria-label="Card back">
    <div class="back-brand">RKW HOLDINGS</div>

    <div class="holder">
      <div class="holder-name">MARCUS OLVANE</div>
      <div class="holder-role">Owner</div>
    </div>

    <div class="divider"></div>

    <ul class="contacts">
      <li>
        <svg viewBox="0 0 16 16" aria-hidden="true"><path d="M4 1.5l2.2 3-1.3 1.5c.8 1.8 2.3 3.3 4.1 4.1l1.5-1.3 3 2.2-1.2 2.5C7 13.2 2.8 9 2 3z" fill="none" stroke="#0a6aa6" stroke-width="1.6" stroke-linejoin="round"/></svg>
        (917) 482-0657
      </li>
      <li>
        <svg viewBox="0 0 16 16" aria-hidden="true"><rect x="1" y="3.5" width="14" height="9" fill="#0a6aa6"/><path d="M1.5 4l6.5 5 6.5-5" fill="none" stroke="#fff" stroke-width="1.2"/></svg>
        marcus@rkwholdings-example.com
      </li>
      <li>
        <svg viewBox="0 0 16 16" aria-hidden="true"><circle cx="8" cy="8" r="6.5" fill="#0a6aa6"/><path d="M1.5 8h13M8 1.5c-2.5 3-2.5 10 0 13M8 1.5c2.5 3 2.5 10 0 13" fill="none" stroke="#fff" stroke-width="1"/></svg>
        www.rkwholdings-example.com
      </li>
    </ul>

    <address class="address">418, 9th Street,<br>Brooklyn NY 11218</address>

    <div class="base-band"></div>
    <div class="base-band-notch"></div>
  </section>
</body>
</html>
```